Caldrey Orthodontics business card

Using our existing logo (created with PixelGuild), please create a tasteful, contemporary business card. We are father and daughter orthodontists specializing in braces, clearvora, etc to design healthy, beautiful smiles for children, adolescents, and adults. We would like the design to be family-friendly but not childish.
The final design should include all of the information without looking cluttered (I hope! If necessary to achieve an optimal design, please consider making the card double-sided)
Purple, black, silver on a white card
Please include the following information:
Caldrey Orthodontics (logo)
Marisol T. Caldrey, DMD
Gordon L. Caldrey, DMD

312 Hollowmere Road
Brierwood, MA 01962
555.214.3096

748C Brackenford Lane
Ashcombe, MA 01973
555.407.1582

email frontdesk@caldreyortho-example.com
website www.caldreyortho-example.com

```html
<!DOCTYPE html>
<html lang="en">
<head>
<meta charset="utf-8">
<title>Caldrey Orthodontics business card</title>
<link rel="stylesheet" href="https://fonts.googleapis.com/css2?family=Fira+Sans:wght@400;600&display=swap">
<style>
  :root {
    --backdrop: #737373;
    --card: #ffffff;
    --purple: #5f2487;
    --grey: #6f6f6f;
    --silver: #9a9a9a;
  }
  html, body {
    margin: 0;
    padding: 0;
    width: 1200px;
    height: 1000px;
    overflow: hidden;
    background: var(--backdrop);
    font-family: "Fira Sans", Arial, sans-serif;
  }
  .stage { position: relative; width: 1200px; height: 1000px; }
  .card {
    position: absolute;
    left: 294px;
    width: 613px;
    height: 352px;
    background: var(--card);
    border-radius: 28px;
    box-shadow: 0 14px 30px rgba(0,0,0,0.35);
    overflow: hidden;
  }
  .card--front { top: 103px; }
  .card--back { top: 496px; }

  .brand {
    display: flex;
    align-items: center;
    gap: 8px;
    color: var(--purple);
    font-weight: 600;
    white-space: nowrap;
  }
  .brand__dot {
    border-radius: 50%;
    background: var(--purple);
    flex: none;
  }
  .card--front .brand {
    position: absolute;
    left: 58px;
    top: 40px;
    font-size: 19px;
  }
  .card--front .brand__dot { width: 14px; height: 14px; }

  .details {
    position: absolute;
    left: 58px;
    top: 102px;
    width: 200px;
    text-align: center;
    color: var(--grey);
  }
  .doctors {
    margin: 0;
    color: var(--purple);
    font-weight: 600;
    font-size: 14.5px;
    line-height: 20px;
  }
  .email { margin: 3px 0 0; font-size: 10.5px; color: var(--grey); }
  .office { margin: 20px 0 0; font-size: 12.5px; line-height: 18px; }
  .office + .office { margin-top: 9px; }
  .office .town { color: var(--purple); }
  .phone { display: inline-flex; align-items: center; gap: 3px; }
  .phone svg { width: 10px; height: 10px; fill: var(--purple); }
  .website {
    margin: 20px 0 0;
    font-size: 13px;
    color: var(--grey);
  }
  .website strong { color: var(--purple); font-weight: 600; }

  .card--back .brand {
    position: absolute;
    left: 50%;
    top: 50%;
    transform: translate(-50%, -50%);
    font-size: 31px;
    gap: 13px;
  }
  .card--back .brand__dot { width: 24px; height: 24px; }
</style>
</head>
<body>
<main class="stage">
  <section class="card card--front" aria-label="Card front">
    <div class="brand"><span class="brand__dot"></span>Caldrey Orthodontics</div>
    <div class="details">
      <p class="doctors">Marisol T. Caldrey, DMD<br>Gordon L. Caldrey, DMD</p>
      <p class="email">frontdesk@caldreyortho-example.com</p>
      <p class="office">312 Hollowmere Road<br><span class="town">Brierwood</span>, MA 01962<br>
        <span class="phone"><svg viewBox="0 0 24 24"><path d="M6.6 10.8a15 15 0 0 0 6.6 6.6l2.2-2.2a1 1 0 0 1 1-.25 11.4 11.4 0 0 0 3.6.57 1 1 0 0 1 1 1V20a1 1 0 0 1-1 1A17 17 0 0 1 3 4a1 1 0 0 1 1-1h3.5a1 1 0 0 1 1 1c0 1.25.2 2.45.57 3.57a1 1 0 0 1-.25 1z"/></svg>555-214-3096</span></p>
      <p class="office">748C Brackenford Lane<br><span class="town">Ashcombe</span>, MA 01973<br>
        <span class="phone"><svg viewBox="0 0 24 24"><path d="M6.6 10.8a15 15 0 0 0 6.6 6.6l2.2-2.2a1 1 0 0 1 1-.25 11.4 11.4 0 0 0 3.6.57 1 1 0 0 1 1 1V20a1 1 0 0 1-1 1A17 17 0 0 1 3 4a1 1 0 0 1 1-1h3.5a1 1 0 0 1 1 1c0 1.25.2 2.45.57 3.57a1 1 0 0 1-.25 1z"/></svg>555-407-1582</span></p>
      <p class="website"><strong>caldreyortho-example</strong>.com</p>
    </div>
  </section>

  <section class="card card--back" aria-label="Card back">
    <div class="brand"><span class="brand__dot"></span>Caldrey Orthodontics</div>
  </section>
</main>
</body>
</html>
```